KVT Calculator

We have a calculator already created however the design seems to be very boring and bland. The calculators goal is to show graphic designers, web development firms, pr agencies, marketing firms how much revenue they can potentially make by offering a managed social media solution to their clients.

We want a great designer to make the calculator appealing to our audience.

It is an amazing offer and opportunity however I do not believe the current design does it justice

you can view and play with calculator live at http://sandbox.plivoran.com/tkna/

```html
<!DOCTYPE html>
<html lang="en">
<head>
<meta charset="utf-8">
<title>Profit Calculator</title>
<link rel="stylesheet" href="https://fonts.googleapis.com/css2?family=Open+Sans:wght@400;600&display=swap">
<style>
:root{
  --sky:#0a97f1;
  --panel:#333333;
  --ink:#ffffff;
  --basic:#29a9e3;
  --pro:#f7941d;
  --enterprise:#3bb54a;
  --rule:#e6e6e6;
  --slider-face:#efefef;
  --slider-grid:#d2d2d2;
  --track-light:#e4e4ea;
  --track-dark:#6b6b6b;
  --btn:#1a1a1a;
}
*{box-sizing:border-box;margin:0;padding:0}
html,body{width:1200px;height:800px;overflow:hidden}
body{background:var(--sky);font-family:"Open Sans",Arial,sans-serif;color:var(--ink);position:relative}
.abs{position:absolute}
.tab{top:163px;height:46px;display:flex;align-items:center;justify-content:center;font-size:19px;letter-spacing:3px;color:var(--ink)}
.tab-basic{left:512px;width:204px;background:var(--basic);border-radius:44px 8px 0 0}
.tab-basic{width:199px}
.tab-pro{left:723px;width:190px;background:var(--pro);border-radius:8px 8px 0 0}
.tab-enterprise{left:920px;width:200px;background:var(--enterprise);border-radius:8px 44px 0 0}
.panel{left:81px;top:208px;width:1040px;height:431px;background:var(--panel);border-radius:4px;border-bottom:2px solid var(--ink)}
.term{left:121px;top:163px;width:116px;height:474px;border:2px solid #1b1b1b;border-radius:4px;overflow:hidden;
  background-color:var(--slider-face);
  background-image:linear-gradient(var(--slider-grid) 1px,transparent 1px),linear-gradient(90deg,var(--slider-grid) 1px,transparent 1px);
  background-size:9px 9px}
.term-head{height:44px;background:var(--panel);display:flex;align-items:center;justify-content:center;font-size:15px;letter-spacing:.6px;border-bottom:2px solid #1b1b1b;white-space:nowrap}
.term-svg{position:absolute;left:0;top:0}
.label{left:276px;font-size:15.5px;letter-spacing:2px;width:236px;height:30px;line-height:30px;white-space:nowrap}
.rule{height:1px;background:var(--rule)}
.divider{top:228px;width:2px;height:244px;background:var(--ink)}
.cell{height:30px;line-height:30px;text-align:center;font-size:18.5px;letter-spacing:1.1px;white-space:nowrap}
.btn{width:32px;height:32px;border-radius:50%;background:var(--btn);border:2px solid var(--ink);display:flex;align-items:center;justify-content:center;font-size:24px;line-height:1;font-weight:600}
.bar{top:486px;height:23px;border-radius:3px}
.total{right:98px;top:560px;font-size:35px;letter-spacing:1.2px;white-space:nowrap}
</style>
</head>
<body>
<div class="abs tab tab-basic">BASIC</div>
<div class="abs tab tab-pro">PRO</div>
<div class="abs tab tab-enterprise">ENTERPRISE</div>

<div class="abs panel"></div>

<div class="abs term">
  <div class="term-head">TERM (YRS)</div>
  <svg class="term-svg" width="116" height="474" viewBox="0 0 116 474">
    <defs>
      <radialGradient id="knob" cx="45%" cy="40%" r="60%">
        <stop offset="0" stop-color="#f4f4f4"/><stop offset="1" stop-color="#9a9a9a"/>
      </radialGradient>
    </defs>
    <g stroke="#1a1a1a" stroke-width="2">
      <line x1="25" y1="84" x2="47" y2="84"/><line x1="65" y1="84" x2="86" y2="84"/>
      <line x1="25" y1="120" x2="47" y2="120"/><line x1="65" y1="120" x2="86" y2="120"/>
      <line x1="25" y1="156" x2="47" y2="156"/><line x1="65" y1="156" x2="86" y2="156"/>
      <line x1="25" y1="192" x2="47" y2="192"/><line x1="65" y1="192" x2="86" y2="192"/>
      <line x1="25" y1="228" x2="47" y2="228"/><line x1="65" y1="228" x2="86" y2="228"/>
      <line x1="25" y1="264" x2="47" y2="264"/><line x1="65" y1="264" x2="86" y2="264"/>
      <line x1="25" y1="336" x2="47" y2="336"/><line x1="65" y1="336" x2="86" y2="336"/>
      <line x1="25" y1="372" x2="47" y2="372"/><line x1="65" y1="372" x2="86" y2="372"/>
      <line x1="25" y1="408" x2="47" y2="408"/><line x1="65" y1="408" x2="86" y2="408"/>
    </g>
    <rect x="47" y="77" width="18" height="358" rx="6" fill="var(--track-light)" stroke="#c4c4c4"/>
    <rect x="47" y="300" width="18" height="135" rx="6" fill="var(--track-dark)"/>
    <circle cx="57" cy="305" r="25" fill="url(#knob)" stroke="#8a8a8a"/>
    <circle cx="57" cy="305" r="19" fill="none" stroke="#cfcfcf"/>
    <polyline points="50,309 57,301 64,309" fill="none" stroke="#444" stroke-width="2"/>
  </svg>
</div>

<div class="abs label" style="top:232px">Clients per month:</div>
<div class="abs rule" style="left:276px;top:284px;width:221px"></div>
<div class="abs label" style="top:298px">You pay:</div>
<div class="abs rule" style="left:276px;top:348px;width:221px"></div>
<div class="abs label" style="top:372px">Your client pays:</div>
<div class="abs rule" style="left:276px;top:424px;width:221px"></div>
<div class="abs label" style="top:448px">Monthly profit (year 4):</div>

<div class="abs divider" style="left:511px"></div>
<div class="abs divider" style="left:711px"></div>
<div class="abs divider" style="left:916px"></div>

<!-- Basic column -->
<div class="abs btn" style="left:518px;top:228px">-</div>
<div class="abs cell" style="left:522px;top:230px;width:176px">1</div>
<div class="abs btn" style="left:672px;top:228px">+</div>
<div class="abs rule" style="left:522px;top:284px;width:176px"></div>
<div class="abs cell" style="left:522px;top:296px;width:176px">$197</div>
<div class="abs rule" style="left:522px;top:348px;width:176px"></div>
<div class="abs btn" style="left:518px;top:370px">-</div>
<div class="abs cell" style="left:522px;top:371px;width:176px">$297</div>
<div class="abs btn" style="left:672px;top:370px">+</div>
<div class="abs rule" style="left:522px;top:424px;width:176px"></div>
<div class="abs cell" style="left:522px;top:448px;width:176px">$4,800</div>
<div class="abs bar" style="left:517px;width:189px;background:var(--basic)"></div>

<!-- Pro column -->
<div class="abs btn" style="left:721px;top:228px">-</div>
<div class="abs cell" style="left:727px;top:230px;width:176px">3</div>
<div class="abs btn" style="left:874px;top:228px">+</div>
<div class="abs rule" style="left:727px;top:284px;width:176px"></div>
<div class="abs cell" style="left:727px;top:296px;width:176px">$297</div>
<div class="abs rule" style="left:727px;top:348px;width:176px"></div>
<div class="abs btn" style="left:721px;top:370px">-</div>
<div class="abs cell" style="left:727px;top:371px;width:176px">$347</div>
<div class="abs btn" style="left:874px;top:370px">+</div>
<div class="abs rule" style="left:727px;top:424px;width:176px"></div>
<div class="abs cell" style="left:727px;top:448px;width:176px">$7,200</div>
<div class="abs bar" style="left:720px;width:188px;background:var(--pro)"></div>

<!-- Enterprise column -->
<div class="abs btn" style="left:927px;top:228px">-</div>
<div class="abs cell" style="left:933px;top:230px;width:175px">2</div>
<div class="abs btn" style="left:1080px;top:228px">+</div>
<div class="abs rule" style="left:933px;top:284px;width:175px"></div>
<div class="abs cell" style="left:933px;top:296px;width:175px">$2500</div>
<div class="abs rule" style="left:933px;top:348px;width:175px"></div>
<div class="abs btn" style="left:927px;top:370px">-</div>
<div class="abs cell" style="left:933px;top:371px;width:175px">$4000</div>
<div class="abs btn" style="left:1080px;top:370px">+</div>
<div class="abs rule" style="left:933px;top:424px;width:175px"></div>
<div class="abs cell" style="left:933px;top:448px;width:175px">$144,000</div>
<div class="abs bar" style="left:926px;width:188px;background:var(--enterprise)"></div>

<div class="abs rule" style="left:276px;top:538px;width:840px;height:2px;background:var(--ink)"></div>
<div class="abs total">Monthly profit by the end of year 4: $156,000</div>
</body>
</html>
```